Personal Finance Author needs a postcard

Hi there,

I am a Canadian personal finance author and have published a new book called The Wealth Compass.

I teach Millennials how to create a 6-figure portfolio through investing (https://www.dariafelt.com/)

I'm speaking at some conferences so we were going to print some postcards to hand out to attendees with our info and calls-to-action on them.

I am looking for 4x6 (horizontal) postcard (no space needed for shipping label).

Logos, Headshots and Book Cover:
https://files.cloudvaultex.com/folders/8kQpZrT2mWvN4xLbJ7sHdYc3FgA9eUoRi?usp=sharing

Both sides will be full colour. I would like a clean and simple look. Our main sites are www.DariaFelt.com and www.TheWealthCompassBook.com if you want to get a sense of style and design.
I also uploaded a few marketing materials so you can see the existing designs.

Side 1:
Get Instant Access to your Free Resources - main headline

(small bullets underneath)
- The Wealth Compass Checklist
- Financial Worksheets
- Database of Investment Tools

DariaFelt.com/Resources

At the bottom, include "Don't forget to follow Daria Felt on social media:
Linkedin: @dariafelt7
Facebook: @thewealthcompassbook Instagram: @thewealthcompassbook Twitter: @WealthCompassBk"

Side 2:
Headline - Want to work directly with Daria and The Wealth Compass team to help you make your money grow and stay safe?

Work with us to (bullet point list)...
- Hire Daria as a Keynote Speaker
- Teach Financial Literacy Workshops
- Receive Financial Coaching

Want To Learn More About How We Can Help?
DariaFelt.com/Services

Include my contact info:
Daria Felt
Author | Speaker | Investor
daria@thewealthcompassbook.com
416-555-0187

Target Market(s)

Millennials who want to learn how to save and invest their money. I focus on stock market investing, real estate investing and entrepreneurship.

Industry/Entity Type

Financial Service

Font styles to use
Sans Serif

Colors

Designer to choose colors to be used in the design.

Requirements
Must have
• Photo of Daria Felt
• The Wealth Compass logo
• Green, Gold/Yellow to match existing colours
• modern business style postcard

```html
<!DOCTYPE html>
<html lang="en">
<head>
<meta charset="utf-8">
<title>The Wealth Compass – Conference Postcards</title>
<link href="https://fonts.googleapis.com/css2?family=Bebas+Neue&family=Signika:wght@400;500;600;700&display=swap" rel="stylesheet">
<style>
  :root {
    --green: #1b6a36;
    --green-soft: #a4b9a4;
    --gold: #ecb02c;
    --paper: #f8f8f5;
    --cream: #f5ecd2;
    --line: #4a4a4a;
    --stage: #e9e9e9;
    --photo-a: #c9b8aa;
    --photo-b: #2a2a33;
  }
  * { margin: 0; padding: 0; box-sizing: border-box; }
  html, body { width: 1200px; height: 504px; overflow: hidden; }
  body {
    background: var(--stage);
    font-family: "Signika", "Trebuchet MS", sans-serif;
    position: relative;
  }
  .postcard {
    position: absolute;
    top: 84px;
    width: 504px;
    height: 336px;
    background: var(--paper);
    overflow: hidden;
  }
  .postcard--front { left: 84px; }
  .postcard--back { left: 611px; }

  .abs { position: absolute; }

  /* brand wordmark */
  .wordmark {
    font-family: "Bebas Neue", "Arial Narrow", sans-serif;
    color: var(--green);
    text-align: center;
    line-height: 0.9;
    white-space: nowrap;
  }
  .wordmark span { display: block; }
  .wordmark__the { font-size: 14px; line-height: 1; }

  /* photo areas */
  .photo {
    background: linear-gradient(180deg, var(--photo-a) 0%, var(--photo-a) 32%, var(--photo-b) 60%, var(--photo-b) 100%);
  }

  /* social row */
  .social {
    left: 0; right: 0;
    top: 303px; height: 33px;
    display: flex;
    align-items: center;
    justify-content: center;
    gap: 8px;
    font-size: 9px;
  }
  .social__item { display: flex; align-items: center; gap: 4px; white-space: nowrap; }
  .social__dot { width: 15px; height: 15px; border-radius: 50%; flex: none; }

  /* ---------- front ---------- */
  .front__swoosh { left: 0; top: 0; width: 504px; height: 336px; }
  .front__photo { left: 16px; top: 8px; width: 186px; height: 295px; z-index: 3; border-radius: 93px 93px 0 0; }
  .front__wordmark { left: 396px; top: 33px; width: 88px; }
  .front__wordmark .wordmark__main { font-size: 31px; }
  .front__headline {
    right: 20px; top: 118px;
    font-family: "Bebas Neue", "Arial Narrow", sans-serif;
    font-weight: 400;
    font-size: 34px; line-height: 34px;
    color: var(--green);
    text-align: right;
    white-space: nowrap;
  }
  .front__bullets {
    left: 207px; right: 0; top: 194px; height: 62px;
    background: var(--gold);
    display: flex; flex-direction: column; justify-content: center; align-items: center;
    list-style: none;
    font-size: 12.6px; line-height: 16.5px; font-weight: 500;
    color: var(--green);
  }
  .front__bullets li::before { content: "\2022"; margin-right: 4px; }
  .front__url {
    left: 207px; right: 0; top: 258px;
    text-align: center;
    font-size: 16px; font-style: italic; font-weight: 600;
    color: var(--green);
  }
  .front__follow {
    left: 0; right: 0; top: 285px; height: 18px;
    background: var(--gold);
    padding-left: 200px;
    display: flex; align-items: center; justify-content: center;
    font-size: 8.5px; font-style: italic; font-weight: 700;
    color: var(--green);
    text-transform: uppercase;
  }
  .front__social { background: var(--green); color: var(--cream); font-style: italic; }
  .front__social .social__dot { background: var(--gold); }

  /* ---------- back ---------- */
  .back__panel {
    left: 0; top: 0; width: 277px; height: 139px;
    background: var(--gold);
    border-bottom-right-radius: 110px 130px;
  }
  .back__intro {
    left: 27px; top: 23px; width: 205px;
    font-size: 11.5px; line-height: 12.6px; font-weight: 500;
    color: var(--green);
  }
  .back__rule {
    left: 0; top: 68px; width: 253px; height: 2px;
    background: linear-gradient(90deg, var(--green) 70%, rgba(27,106,54,0));
  }
  .back__services {
    left: 27px; top: 75px;
    list-style: none;
    font-size: 13.5px; line-height: 16.8px; font-weight: 500;
    color: var(--green);
    white-space: nowrap;
  }
  .back__wordmark { left: 285px; top: 22px; width: 98px; }
  .back__wordmark .wordmark__main { font-size: 34px; }
  .back__stamp { left: 399px; top: 21px; width: 84px; height: 83px; background: var(--gold); }
  .back__cta {
    left: 93px; width: 160px; top: 153px;
    text-align: center;
    font-family: "Bebas Neue", "Arial Narrow", sans-serif;
    font-size: 17px; line-height: 20px;
    color: var(--green);
    white-space: nowrap;
  }
  .back__contact-bg {
    left: 72px; top: 229px; width: 205px; height: 75px;
    background: var(--green);
    border-top-right-radius: 70px 75px;
  }
  .back__photo { left: 0; top: 142px; width: 104px; height: 162px; z-index: 3; border-radius: 52px 52px 0 0; }
  .back__contact { left: 110px; top: 233px; color: var(--gold); white-space: nowrap; }
  .back__name { font-size: 17px; font-weight: 600; line-height: 20px; }
  .back__role { font-size: 9.5px; line-height: 11px; font-weight: 500; }
  .back__email { font-size: 9.5px; line-height: 11px; color: var(--cream); }
  .back__phone { font-size: 17px; font-weight: 600; line-height: 20px; }
  .back__address-line { left: 279px; width: 204px; height: 1.5px; background: var(--line); }
  .back__social { background: var(--gold); color: var(--green); }
  .back__social .social__dot { background: var(--green); }
</style>
</head>
<body>

<section class="postcard postcard--front" aria-label="Postcard front">
  <svg class="abs front__swoosh" viewBox="0 0 504 336" aria-hidden="true">
    <path d="M252 0 C 200 40 150 110 110 210 L 140 210 C 180 115 232 45 289 0 Z" fill="var(--green-soft)"/>
    <path d="M284 0 C 235 40 195 95 168 175 L 186 175 C 215 95 290 35 383 0 Z" fill="var(--green)"/>
  </svg>

  <div class="abs photo front__photo" role="img" aria-label="Portrait photo of Daria Felt in a dark blazer"></div>

  <div class="abs wordmark front__wordmark">
    <span class="wordmark__the">The</span>
    <span class="wordmark__main">Wealth</span>
    <span class="wordmark__main">Compass</span>
  </div>

  <h1 class="abs front__headline">Get Instant Access To<br>Your Free Resources</h1>

  <ul class="abs front__bullets">
    <li>The Wealth Compass Checklist</li>
    <li>Financial Worksheets</li>
    <li>Database of Investment Tools</li>
  </ul>

  <p class="abs front__url">DariaFelt.com/Resources</p>

  <p class="abs front__follow">Don't forget to follow Daria Felt on social media</p>

  <div class="abs social front__social">
    <span class="social__item"><span class="social__dot"></span>@dariafelt7</span>
    <span class="social__item"><span class="social__dot"></span>@thewealthcompassbook</span>
    <span class="social__item"><span class="social__dot"></span>@thewealthcompassbook</span>
    <span class="social__item"><span class="social__dot"></span>@WealthCompassBk</span>
  </div>
</section>

<section class="postcard postcard--back" aria-label="Postcard back">
  <div class="abs back__panel"></div>
  <p class="abs back__intro">Want to work directly with Daria and The Wealth Compass team to help you make your money grow and stay safe?</p>
  <div class="abs back__rule"></div>
  <ul class="abs back__services">
    <li>Hire Daria as a Keynote Speaker</li>
    <li>Teach Financial Literacy Workshops</li>
    <li>Receive Financial Coaching</li>
  </ul>

  <div class="abs wordmark back__wordmark">
    <span class="wordmark__the">The</span>
    <span class="wordmark__main">Wealth</span>
    <span class="wordmark__main">Compass</span>
  </div>
  <div class="abs back__stamp"></div>

  <p class="abs back__cta">Want to learn more about<br>how we can help?<br>DariaFelt.com/Services</p>

  <div class="abs back__address-line" style="top:222px"></div>
  <div class="abs back__address-line" style="top:257px"></div>
  <div class="abs back__address-line" style="top:292px"></div>

  <div class="abs back__contact-bg"></div>
  <div class="abs photo back__photo" role="img" aria-label="Headshot photo of Daria Felt"></div>
  <div class="abs back__contact">
    <p class="back__name">DARIA FELT</p>
    <p class="back__role">Author | Speaker | Investor</p>
    <p class="back__email">daria@thewealthcompassbook.com</p>
    <p class="back__phone">416-555-0187</p>
  </div>

  <div class="abs social back__social">
    <span class="social__item"><span class="social__dot"></span>@dariafelt7</span>
    <span class="social__item"><span class="social__dot"></span>@thewealthcompassbook</span>
    <span class="social__item"><span class="social__dot"></span>@thewealthcompassbook</span>
    <span class="social__item"><span class="social__dot"></span>@WealthCompassBk</span>
  </div>
</section>

</body>
</html>
```